Website for Strategy and proejct Management Business Advisory Firm

Create a new a fresh design to replace my existing website (www.kvrm48.com). We have a business advisory firm specializing in strategic planning, project management, and business process development among other things.

I would like to move away from narrative content and make the site seem more infographic in nature. No stock photos and more custom desinged images.

The result would be a site that is easy to navigate, content that is easy to consume, and overall leaves the viewer with a positive experience.

Our logo is black and red and I like blues and whites as well. Happy to review other color schemes though.

It would basically be a brochure site, but I would like to be able post news or a blog capability.

Our current site is hosted with HostMoxie. I would need the files necessary to stand up the site in their environment. Ideally, the designer could handle this for me as I do not have expertise in this area.

Some questions I have - will I be able to update content? Can I make revisions during the design process?

Thank you!!

Target Market(s)

Mostly small to medium size businesses although the planning framework I use and the project management methodology applies to any business segment, both for and not for profit.

Industry/Entity Type

Consulting

Coding

Coded - Design and coding required

Number of Pages Required

5+ page

Font styles to use
Sans Serif

Colors
85acd3
3277b5
0355a3
f04a50
ec1f27
0393ce

Requirements
Must have
• Infograph or icon driven look and feel. Professional yet elegant. Pages that address the nature of the company, the services we offer, brief testimonials, display logos of clients and an ability to post news or blog content.
Nice to have
• Perhaps something that is on the cool/fun side.
Should not have
• A lot of text, stock photos, broken links, content that cannot be edited easily.

```html
<!DOCTYPE html>
<html lang="en">
<head>
<meta charset="utf-8">
<title>Harrowgate Strategy Group</title>
<link href="https://fonts.googleapis.com/css2?family=Arimo:ital,wght@0,400;0,700;1,400&display=swap" rel="stylesheet">
<style>
:root{
  --blue:#0355a3;
  --blue-mid:#3277b5;
  --blue-light:#85acd3;
  --sky:#0393ce;
  --navy:#16237a;
  --ink:#222831;
  --text:#555b66;
  --muted:#8a9099;
  --line:#d9dde3;
  --soft:#f4f5f8;
  --white:#ffffff;
}
*{box-sizing:border-box;margin:0;padding:0}
html,body{width:1200px;height:3396px;overflow:hidden}
body{font-family:"Arimo",Arial,sans-serif;color:var(--text);background:var(--white);position:relative}
a{color:inherit;text-decoration:none}

/* hero */
.hero{position:absolute;left:0;top:0;width:1200px;height:543px;background:linear-gradient(180deg,#1d6bb8 0%,#2a7fc6 55%,#2f86cc 100%)}
.hero-chart{position:absolute;left:0;top:360px}
.site-header{position:absolute;left:0;top:0;width:1200px;height:68px;background:rgba(10,70,140,.45);display:flex;align-items:center;padding:0 50px}
.logo{color:var(--white);font-size:17px;font-weight:700;width:300px;white-space:nowrap}
.main-nav{display:flex;gap:48px;margin-left:96px;color:var(--white);font-size:14px;font-weight:700;letter-spacing:.3px}
.header-actions{margin-left:auto;display:flex;align-items:center;gap:20px;color:var(--white);font-size:14px;font-weight:700}
.btn-inquire{background:var(--white);color:var(--ink);border-radius:16px;padding:8px 18px}

/* intro */
.intro{position:absolute;left:0;top:543px;width:1200px;height:170px;text-align:center}
.intro-lead{margin:18px auto 0;width:1000px;font-size:19px;line-height:1.38;color:var(--ink)}
.intro-sub{font-size:12px;margin-top:10px}
.btn-start{display:inline-flex;align-items:center;gap:8px;margin-top:18px;border:2px solid var(--blue);color:var(--blue);border-radius:18px;padding:8px 20px;font-size:12px;font-weight:700}

/* section headings */
.section-title{text-align:center;font-size:22px;font-weight:700;color:var(--ink)}
.section-title span{color:var(--blue)}
.dots{border-top:2px dotted var(--blue-light);width:1096px;margin:16px auto 0}

/* services */
.services{position:absolute;left:0;top:713px;width:1200px;height:496px;background:var(--soft);padding-top:22px;border-top:1px solid var(--line)}
.service-list{display:flex;justify-content:space-between;width:1110px;margin:56px auto 0}
.service{width:210px;text-align:center}
.service svg{height:92px;width:100px}
.service h3{font-size:18px;color:var(--ink);line-height:1.3;margin:14px auto 0;min-height:50px;max-width:160px}
.service:nth-child(2) h3{max-width:210px}
.service p{font-size:12.5px;line-height:1.55;margin:14px auto 0;max-width:196px}

/* about */
.about-band{position:absolute;left:0;top:1499px;width:1200px;height:466px;background:linear-gradient(90deg,#1b2b86,var(--navy))}
.about-photo{position:absolute;left:258px;top:1209px;width:686px;height:414px;background:linear-gradient(135deg,#dfe6ec 0%,#b9c4cf 55%,#8f9aa6 100%)}
.about-head{position:absolute;left:0;top:1660px;width:1200px;text-align:center;color:var(--white)}
.about-head small{font-size:13px}
.about-head h2{font-size:38px;font-weight:400;margin-top:8px}
.partners{position:absolute;left:50px;top:1760px;width:1100px;display:flex;gap:36px;color:var(--white)}
.partner{flex:1;text-align:center}
.partner h4{font-size:17px}
.partner p{font-size:12.5px;line-height:1.5;margin-top:10px}
.partner a{display:block;margin-top:18px;font-size:13px;font-weight:700}

/* news */
.news{position:absolute;left:0;top:1965px;width:1200px;height:503px;padding-top:30px}
.cards{display:flex;gap:28px;width:1100px;margin:56px auto 0}
.card{width:253px;background:var(--soft)}
.card-img{height:190px}
.card-body{padding:18px 18px 14px}
.card-body h3{font-size:17px;color:var(--ink)}
.card-body p{font-size:12.5px;line-height:1.5;margin-top:8px}
.card-meta{display:flex;justify-content:space-between;font-size:11px;color:var(--muted);margin-top:18px}

/* testimonials */
.quotes{position:absolute;left:0;top:2468px;width:1200px;height:410px;background:var(--soft);padding-top:30px}
.quote-grid{position:absolute;left:50px;top:104px;width:1100px;height:248px;display:grid;grid-template-columns:1fr 1fr;grid-template-rows:1fr 1fr}
.quote-grid::before{content:"";position:absolute;left:550px;top:0;height:100%;border-left:1px dotted #aab2bd}
.quote-grid::after{content:"";position:absolute;left:0;top:124px;width:100%;border-top:1px dotted #aab2bd}
.quote{display:flex;align-items:center;gap:22px;padding:0 18px}
.quote.left{text-align:right}
.quote p{font-size:12.5px;font-style:italic;line-height:1.5;color:var(--muted)}
.quote cite{display:block;font-style:normal;color:var(--ink);font-size:12.5px;margin-top:8px}
.avatar{flex:0 0 76px;height:76px;border-radius:50%;background:linear-gradient(135deg,#d8c2b0,#7d6a5d)}

/* contact */
.contact{position:absolute;left:50px;top:2898px;width:1100px;height:310px;display:flex;gap:28px}
.contact h3{font-size:18px;color:var(--ink)}
.mail-form{width:253px}
.mail-form .row{display:flex;gap:16px;margin-top:22px}
.field{border:1px solid #b9c0c9;border-radius:4px;height:32px;font-size:11px;color:var(--muted);padding:9px 14px;flex:1}
.field.full{margin-top:14px}
.field.area{height:70px}
.btn-send{display:inline-block;background:var(--blue);color:var(--white);font-size:12px;font-weight:700;border-radius:16px;padding:9px 20px;margin-top:18px}
.hq{width:534px;text-align:center}
.map{margin-top:20px;height:263px;background:linear-gradient(135deg,#a8c9e6,#dfe8d5 50%,#c9dbe9)}
.info{width:253px}
.info p{font-size:12.5px;line-height:1.6;margin-top:12px}
.info h3.follow{margin-top:20px}
.social{display:flex;gap:12px;margin-top:14px}
.social span{width:26px;height:26px;border-radius:50%;background:var(--blue)}

/* footer */
.site-footer{position:absolute;left:0;top:3235px;width:1200px;height:161px;border-top:4px solid var(--blue);padding:0 50px}
.footer-top{display:flex;align-items:center;margin-top:28px}
.footer-top nav{display:flex;gap:30px;margin-left:26px;font-size:13px;font-weight:700;color:var(--ink)}
.footer-logo{margin-left:auto;font-size:15px;color:var(--ink);white-space:nowrap}
.footer-bottom{display:flex;margin-top:28px;font-size:11px;color:var(--text)}
.footer-bottom nav{display:flex;gap:18px}
.footer-bottom .legal{margin-left:auto;display:flex;gap:18px}
</style>
</head>
<body>

<section class="hero" role="img" aria-label="Blue-toned photo of a desk with laptops and papers">
  <svg class="hero-chart" width="1200" height="150" viewBox="0 0 1200 150">
    <polyline fill="none" stroke="rgba(255,255,255,.45)" stroke-width="2" points="0,40 70,70 140,55 210,90 280,80 350,110 420,95 490,120 560,100 630,60 700,85 770,70 840,95 910,50 980,75 1050,40 1120,60 1200,30"/>
  </svg>
</section>

<header class="site-header">
  <div class="logo">Harrowgate Strategy Group</div>
  <nav class="main-nav"><a>SPECIALTIES</a><a>COMPANY</a><a>CAREERS</a><a>OUR WORK</a></nav>
  <div class="header-actions"><a>Knowledge</a><a class="btn-inquire">Inquire</a></div>
</header>

<section class="intro">
  <p class="intro-lead">Harrowgate Strategy Group is a strategy and planning consulting firm which leverages practical effective, and simple planning techniques to design business strategies and execution frameworks</p>
  <p class="intro-sub">See some of the features below and learn why businesses trust Harrowgate Strategy</p>
  <a class="btn-start"><svg width="10" height="10" viewBox="0 0 10 10"><path d="M1 0 L9 5 L1 10Z" fill="currentColor"/></svg>GET STARTED</a>
</section>

<section class="services">
  <h2 class="section-title">What <span>We Do</span></h2>
  <div class="dots"></div>
  <div class="service-list">
    <article class="service">
      <svg viewBox="0 0 100 92" fill="none" stroke="#0355a3" stroke-width="3"><path d="M5 46 Q50 5 95 46 Q50 87 5 46Z"/><circle cx="50" cy="46" r="18"/><circle cx="50" cy="46" r="7"/><path d="M50 8v-6M30 14l-4-5M70 14l4-5"/></svg>
      <h3>Strategy Management</h3>
      <p>We facilitate and develop enterprise and operational business strategies using proven techniques that save time, money and add value with an emphasis on execution excellence.</p>
    </article>
    <article class="service">
      <svg viewBox="0 0 100 92" fill="none" stroke="#0355a3" stroke-width="3"><rect x="8" y="14" width="76" height="62" rx="3"/><path d="M8 30h76M24 6v14M68 6v14M20 42h10M38 42h10M56 42h10M20 56h10M38 56h10"/><circle cx="78" cy="72" r="14" fill="#fff"/><path d="M71 72l5 5 9-10"/></svg>
      <h3>Portfolio and Project Management (PPM)</h3>
      <p>Executing your strategic plan centers around key projects and operational work. We offer PMP credentialed PMO development, portfolio &amp; project management, and professional development.</p>
    </article>
    <article class="service">
      <svg viewBox="0 0 100 92" fill="none" stroke="#0355a3" stroke-width="3"><rect x="6" y="20" width="80" height="54" rx="3"/><path d="M34 74l-4 12h32l-4-12M2 86h96"/><rect x="50" y="6" width="40" height="26" fill="#fff"/><path d="M56 14h28M56 22h20"/><circle cx="28" cy="44" r="8"/><path d="M16 66q12-16 24 0M50 46h26M50 56h20"/></svg>
      <h3>Business Process</h3>
      <p>Keep the knowledge of your teams from walking out the door – well documented processes allow plug and play of roles no longer relying on specific employees.</p>
    </article>
    <article class="service">
      <svg viewBox="0 0 100 92" fill="none" stroke="#0355a3" stroke-width="3"><circle cx="50" cy="12" r="8"/><path d="M40 32q10-14 20 0M50 34v12M18 46h64M18 46v10M50 46v10M82 46v10"/><circle cx="18" cy="70" r="12"/><circle cx="50" cy="70" r="12"/><circle cx="82" cy="70" r="12"/></svg>
      <h3>Organizational Development</h3>
      <p>Realize transformational change in support of your business strategies by mapping out maturity roadmaps for your product lines, departments, and enterprise capabilities.</p>
    </article>
    <article class="service">
      <svg viewBox="0 0 100 92" fill="none" stroke="#0355a3" stroke-width="3"><rect x="10" y="6" width="22" height="18"/><rect x="68" y="6" width="22" height="18"/><rect x="36" y="36" width="28" height="20"/><rect x="10" y="68" width="22" height="18"/><rect x="68" y="68" width="22" height="18"/><path d="M32 15h36M21 24v22h15M79 24v22H64M50 56v21H32M50 77h18"/></svg>
      <h3>Operational Planning</h3>
      <p>Translate business objectives into actionable and practical work plans. Even with a well-designed strategy, use robust operational plans to keep daily operations running effectively.</p>
    </article>
  </div>
</section>

<div class="about-band"></div>
<div class="about-photo" role="img" aria-label="Portrait photo of a smiling consultant in a suit in a bright office"></div>
<div class="about-head"><small>Our Little Story</small><h2>Something About Us</h2></div>
<section class="partners">
  <div class="partner">
    <h4>Callum Rivett</h4>
    <p>Callum Rivett is a founding partner of Harrowgate Strategy Group – a strategy and planning consultancy. He is responsible for facilitating the development of corporate and business strategies for his clients. Further, Callum develops and implements execution frameworks to help his clients realize their vision and goals.</p>
    <a>Read More</a>
  </div>
  <div class="partner">
    <h4>Neil Vasquell</h4>
    <p>Neil Vasquell is Co-Founder of HSG where he works with organizations to develop practical strategies and supporting execution models. Through the use of a variety of proven tools, methodologies and professional facilitation techniques, HSG has helped multiple organizations define their mission and objectives and the means for achieving them.</p>
    <a>Read More</a>
  </div>
</section>

<section class="news">
  <h2 class="section-title">Latest <span>News &amp; Views</span></h2>
  <div class="dots"></div>
  <div class="cards">
    <article class="card"><div class="card-img" role="img" aria-label="Photo of a traveller walking with a leather bag" style="background:linear-gradient(135deg,#5b4636,#a7764a)"></div>
      <div class="card-body"><h3>Standard Post</h3><p>Enim congue blandit. Lorem ipsum dolor sit amet, consectetur adipiscing elit. Quisque...</p><div class="card-meta"><span>22 June, 2015</span><span>0</span></div></div></article>
    <article class="card"><div class="card-img" role="img" aria-label="Photo of a glass coffee maker on a table" style="background:linear-gradient(135deg,#e9e7e3,#9c8d7c)"></div>
      <div class="card-body"><h3>Video Post</h3><p>Ultrices posuere cubilia curae curabitur sit amet tortor ut massa commodo. Vestibulum...</p><div class="card-meta"><span>22 June, 2015</span><span>0</span></div></div></article>
    <article class="card"><div class="card-img" role="img" aria-label="Photo of a cafe table by a brick wall" style="background:linear-gradient(135deg,#6e4633,#c59a6e)"></div>
      <div class="card-body"><h3>Post with Image</h3><p>Enim congue blandit. Lorem ipsum dolor sit amet, consectetur adipiscing elit. Quisque...</p><div class="card-meta"><span>22 June, 2015</span><span>0</span></div></div></article>
    <article class="card"><div class="card-img" role="img" aria-label="Photo of an open notebook on a desk" style="background:linear-gradient(135deg,#d9cbbb,#8a5a45)"></div>
      <div class="card-body"><h3>Image Post</h3><p>Ultrices posuere cubilia curae curabitur sit amet tortor ut massa commodo. Vestibulum...</p><div class="card-meta"><span>22 June, 2015</span><span>3</span></div></div></article>
  </div>
</section>

<section class="quotes">
  <h2 class="section-title">What <span>People Say</span></h2>
  <div class="quote-grid">
    <div class="quote left"><div><p>Duis aute irure dolor in reprehenderit in voluptate velit esse cillum dolore eu fugiat nulla pariatur. Excepteur sint occaecat cupidatat non proident, sunt in culpa qui officia deserunt mollit.</p><cite>Dara Quell, Operations Manager</cite></div><div class="avatar" role="img" aria-label="Portrait of client"></div></div>
    <div class="quote"><div class="avatar" role="img" aria-label="Portrait of client"></div><div><p>Provident, similique sunt in culpa qui officia deserunt mollitia animi, id est laborum et dolorum fuga. Et harum quidem rerum facilis est et expedita distinctio. Nam libero tempore, cum soluta nobis.</p><cite>Lina Morrow, Creative Designer</cite></div></div>
    <div class="quote left"><div><p>Luis aute irure dolor in reprehenderit in pluptate velit esse cillum dolore eu fugiat nulla pariatur. Excepteur sint occaecat cupidatat non proident, sunt in culpa qui officia deserunt mollit.</p><cite>Mira Tolland, Manager</cite></div><div class="avatar" role="img" aria-label="Portrait of client"></div></div>
    <div class="quote"><div class="avatar" role="img" aria-label="Portrait of client"></div><div><p>At vero eos et accusamus et iusto odio dignissimos ducimus qui blanditiis praesentium voluptatum deleniti atque corrupti quos dolores et quas molestias excepturi sint occaecati asperiores.</p><cite>Tam Hartvik, Developer</cite></div></div>
  </div>
</section>

<section class="contact">
  <div class="mail-form">
    <h3>Feel Free to Mail</h3>
    <div class="row"><div class="field">Name *</div><div class="field">Email *</div></div>
    <div class="field full">Subject</div>
    <div class="field full area">Write Your Message Here...</div>
    <a class="btn-send">SEND MESSAGE</a>
  </div>
  <div class="hq">
    <h3>Headquarters</h3>
    <div class="map" role="img" aria-label="Street map showing the office location near the harbor"></div>
  </div>
  <div class="info">
    <h3>Contact Info</h3>
    <p>Our staff is available to you from 9AM until 5PM on weekdays.</p>
    <p>Phone: +1 (555) 014 27 63</p>
    <p>Office: Pier Nine Office Commons</p>
    <p>Email: info@yourdomain.com</p>
    <h3 class="follow">Follow Us on</h3>
    <div class="social"><span></span><span></span><span></span><span></span><span></span></div>
  </div>
</section>

<footer class="site-footer">
  <div class="footer-top">
    <svg width="14" height="14" viewBox="0 0 14 14" fill="none" stroke="#555b66" stroke-width="2"><circle cx="6" cy="6" r="4.5"/><path d="M9.5 9.5L13 13"/></svg>
    <nav><a>Help &amp; Contact</a><a>Services</a><a>Blog</a><a>Testimonials</a></nav>
    <div class="footer-logo">Harrowgate Strategy Group</div>
  </div>
  <div class="footer-bottom">
    <nav><a>About</a><a>Blog</a><a>Careers</a><a>Public Policy</a><a>Sitemap</a><a>People</a><a>Partners</a></nav>
    <div class="legal"><span>© 2006 - 2018</span><a>Privacy</a><a>Legal</a><a>Feedback</a></div>
  </div>
</footer>

</body>
</html>
```